Website Design for Solar Panel Company

We are working with a company called VoltaryNX.

Some sites to use for content/competitors and inspiration:
https://www.brightmoor.example
https://prod.cld-prod.raylumen.example
https://amberfieldvolt.example
https://www.korvane.example/solarpanels

Thank you for taking the time to consider designing a website for us. We are web developers based in Stockton, CA, USA. Most of our projects go through the same process. Understanding this process may help you win a project with us. We custom-code all of our websites in-house. We don’t have any requirements as to what tools you use for your design, but we prefer Figma files. For any design that we label as four-stars, we send it to the client for review. The client picks the final design they want us to use. Once we complete this process, we will continue to show additional clients all the four-star sites and purchase them later. Your designs will have multiple chances to sell. For better chances of success, we ask that you follow these guidelines.

IMAGES:
If you use any images or icons in the design, we ask that you have a link to the asset so we can purchase the image/icon. Most of the designs we submit do not have the customer’s images on them unless they have some great images. Be creative; show us the feeling you are trying to portray with your image choices. Use any royalty-free site you choose. We subscribe to Quillex and mainly use their images, but we can purchase images outside of Quillex. PLEASE NOTE: we will not submit designs to clients with watermarks on the images.

FONTS:
We ask that you identify the fonts used in the design. This can be done in a message if you want. We typically use Marlowe Fonts and Quillex Fonts.

CONTENT:
We're always open to different content and ideas. We often submit designs with stock images so the client can see our vision. We typically take pictures after the website launch to use their images with our vision. Lorem Ipsum is fine for paragraphs, but we ask that you write the headers in correct English. We want to be able to show the vision and identify the sections of the website.

INSPIRATION:
We typically add a couple of links in the brief of websites we like to help you get started in your design.

REVISIONS:
We do not often ask for revisions of the designs unless we see something in the design that may not appeal to the client. If there are slight changes that we want to make, we do that in the development process.

FEEDBACK:
We rarely give feedback on designs during the design process. We are working on many website projects and do not have the time to provide feedback. We usually respond if your request is well thought out and asks specific questions, but a note asking “feedback, please” usually goes unanswered.

```html
<!DOCTYPE html>
<html lang="en">
<head>
<meta charset="utf-8">
<title>VoltaryNX — Solar Panels for Your Home</title>
<link rel="stylesheet" href="https://fonts.googleapis.com/css2?family=Montserrat:wght@400;500;600;700;800&family=Open+Sans:wght@400;600&display=swap">
<style>
:root{
  --green:#3cc61e;
  --green-light:#7be04a;
  --green-dark:#2a9e12;
  --black:#0b0b0b;
  --ink:#1c1c1c;
  --text:#6b6b6b;
  --white:#ffffff;
  --field:#eeeeee;
  --line:#e2e2e2;
}
*{box-sizing:border-box;margin:0;padding:0}
html,body{width:1200px;height:4964px;overflow:hidden}
body{position:relative;background:var(--white);font-family:'Open Sans',Arial,sans-serif;color:var(--text);font-size:15px;line-height:1.55}
h1,h2,h3,h4,.btn,.eyebrow,.brand,.nav a{font-family:'Montserrat',Arial,sans-serif}
.abs{position:absolute}
.btn{display:inline-flex;align-items:center;justify-content:center;height:44px;padding:0 30px;border-radius:3px;background:linear-gradient(90deg,var(--green),var(--green-light));color:var(--white);font-size:13px;font-weight:700;text-transform:uppercase;letter-spacing:.5px;text-decoration:none}
.btn--dark{background:var(--black)}
.eyebrow{color:var(--green);font-size:16px;font-weight:700;text-transform:uppercase;letter-spacing:.5px}
.brand{color:var(--white);font-size:34px;font-weight:800;letter-spacing:1px;display:flex;align-items:center;gap:10px}
.brand::before{content:"";width:14px;height:14px;background:var(--green)}

/* Top bar */
.topbar{position:absolute;left:0;top:0;width:1200px;height:120px;background:var(--black)}
.topbar .brand{position:absolute;left:128px;top:38px}
.contact-item{position:absolute;top:40px;display:flex;gap:12px;color:var(--white);font-size:14px;line-height:1.3}
.contact-item small{display:block;color:var(--green);font-size:13px}
.topbar .btn{position:absolute;left:900px;top:40px;height:42px;padding:0 28px}

/* Hero */
.hero{position:absolute;left:0;top:120px;width:1200px;height:700px;background:linear-gradient(180deg,#6f7d86 0%,#3f4a4b 45%,#2f3a2b 75%,#4a5b33 100%)}
.nav{position:absolute;left:128px;top:130px;width:944px;height:60px;background:var(--white);display:flex;align-items:center;padding:0 20px;gap:44px;box-shadow:0 4px 14px rgba(0,0,0,.15)}
.nav a{color:var(--ink);font-size:13px;font-weight:700;text-decoration:none;text-transform:uppercase;display:flex;align-items:center;gap:6px}
.nav a.active{color:var(--green)}
.hero h1{position:absolute;left:132px;top:288px;color:var(--white);font-size:50px;font-weight:700;line-height:1.15}
.hero .btn{position:absolute;left:132px;top:420px}

/* Feature cards */
.feature{position:absolute;top:700px;width:280px;height:350px;background:var(--white);box-shadow:0 6px 22px rgba(0,0,0,.12);padding:52px 28px 0;text-align:center}
.feature h3{color:var(--ink);font-size:17px;font-weight:700;line-height:1.3;margin:18px 0 14px}
.feature p{font-size:13px;line-height:1.5}
.feature--accent{background:linear-gradient(180deg,var(--green-light),var(--green));color:var(--white)}
.feature--accent h3{color:var(--white);margin-top:70px}
.feature--accent .btn{margin-top:22px;height:40px}

/* Welcome */
.welcome-photo{position:absolute;left:128px;top:1200px;width:342px;height:420px;background:linear-gradient(180deg,#c9cfd3,#7b868c 60%,#3d474c)}
.welcome-frame{position:absolute;left:250px;top:1296px;width:260px;height:270px;border:16px solid var(--green);background:linear-gradient(180deg,#bfd2de,#e6e6e2 55%,#6b7e52)}
.welcome-text{position:absolute;left:665px;top:1228px;width:410px}
.welcome-text h2{color:var(--ink);font-size:26px;font-weight:700;line-height:1.3;margin:10px 0 22px}
.welcome-text p{font-size:13px;margin-bottom:18px}
.welcome-text .btn{margin-top:14px}

/* Services */
.section-head{position:absolute;left:0;width:1200px;text-align:center}
.section-head h2{color:var(--ink);font-size:28px;font-weight:700;margin-top:8px}
.service{position:absolute;top:1992px;width:300px;height:530px;background:var(--white);box-shadow:0 6px 22px rgba(0,0,0,.1)}
.service .photo{height:230px}
.service h3{color:var(--ink);font-size:22px;font-weight:700;line-height:1.25;margin:28px 24px 12px}
.service p{font-size:14px;margin:0 24px 24px}
.service .btn{margin-left:24px;height:44px}

/* Quote band */
.quote-band{position:absolute;left:0;top:2782px;width:1200px;height:400px;background:linear-gradient(90deg,#1b1c18 0%,#3a3a2e 55%,#2a2c22 100%)}
.quote-band h2{position:absolute;left:132px;top:16px;color:var(--white);font-size:32px;font-weight:700;line-height:1.2}
.quote-band p{position:absolute;left:132px;top:100px;width:330px;color:#e6e6e6;font-size:14px}
.quote-band .btn{position:absolute;left:132px;top:240px}
.quote-form{position:absolute;left:620px;top:2688px;width:460px;height:700px;background:var(--white);box-shadow:0 10px 30px rgba(0,0,0,.2);padding:50px 36px 0}
.quote-form::after{content:"";position:absolute;right:0;top:0;border-style:solid;border-width:0 60px 60px 0;border-color:transparent var(--green) transparent transparent}
.quote-form h3{color:var(--ink);font-size:26px;font-weight:800;line-height:1.2;text-transform:uppercase;margin-bottom:30px}
.row{display:flex;gap:10px;margin-bottom:14px}
.field{flex:1;height:52px;background:var(--field);padding:0 14px;display:flex;align-items:center;font-size:13px;color:#777}
.field--tall{height:52px}
.check{display:flex;align-items:center;gap:12px;color:var(--ink);font-size:13px;margin:24px 0 30px}
.check span{width:26px;height:26px;border:1px solid #999;background:var(--white)}
.quote-form .btn{display:flex;width:210px;margin:0 auto;height:50px}

/* Financing */
.finance-photo{position:absolute;left:128px;top:3620px;width:476px;height:430px;background:linear-gradient(135deg,#d9d2c6,#a9988a 50%,#6d645c)}
.finance-box{position:absolute;left:620px;top:3660px;width:452px;height:340px;background:var(--white);box-shadow:0 6px 22px rgba(0,0,0,.1);padding:44px 36px}
.finance-box h3{color:var(--ink);font-size:26px;font-weight:800;line-height:1.2;text-transform:uppercase;margin-bottom:14px}
.finance-box p{font-size:14px;margin-bottom:24px}

/* CTA */
.cta{position:absolute;left:0;top:4190px;width:1200px;height:290px;background:linear-gradient(120deg,var(--green-dark),var(--green) 45%,var(--green-light));text-align:center;color:var(--white);padding-top:78px}
.cta h2{font-size:40px;font-weight:800;text-transform:uppercase;letter-spacing:.5px}
.cta p{width:540px;margin:12px auto 24px;font-size:14px}

/* Footer */
.footer{position:absolute;left:0;top:4480px;width:1200px;height:484px;background:var(--black);color:#cfcfcf;font-size:14px}
.footer .brand{position:absolute;left:128px;top:120px;font-size:32px}
.footer .legal{position:absolute;left:128px;top:184px;font-size:13px;line-height:1.7}
.footer-col{position:absolute;top:120px}
.footer-col h4{color:var(--green);font-size:18px;font-weight:700;margin-bottom:22px;display:flex;align-items:center;gap:12px}
.footer-col h4::before{content:"";width:3px;height:20px;background:var(--green)}
.footer-col li{list-style:none;margin-bottom:10px}
.contact-line{display:flex;gap:12px;margin-bottom:14px;line-height:1.45}
.newsletter-input{width:260px;height:44px;background:var(--white);margin:18px 0 14px}
.footer .btn{width:260px}
</style>
</head>
<body>

<header class="topbar">
  <div class="brand">VoltaryNX</div>
  <div class="contact-item" style="left:380px">
    <svg width="22" height="18" viewBox="0 0 22 18" fill="none" stroke="#3cc61e" stroke-width="2"><rect x="1" y="1" width="20" height="16" rx="2"/><path d="M1 3l10 7 10-7"/></svg>
    <div><small>Email Address</small>info@voltarynx.example</div>
  </div>
  <div class="contact-item" style="left:680px">
    <svg width="20" height="20" viewBox="0 0 24 24" fill="none" stroke="#3cc61e" stroke-width="2"><path d="M22 16.9v3a2 2 0 0 1-2.2 2 19.8 19.8 0 0 1-8.6-3.1 19.5 19.5 0 0 1-6-6A19.8 19.8 0 0 1 2.1 4.2 2 2 0 0 1 4.1 2h3a2 2 0 0 1 2 1.7c.1 1 .4 1.9.7 2.8a2 2 0 0 1-.5 2.1L8 9.9a16 16 0 0 0 6 6l1.3-1.3a2 2 0 0 1 2.1-.4c.9.3 1.8.6 2.8.7a2 2 0 0 1 1.8 2z"/></svg>
    <div><small>Phone Number</small>+44 (0)000 240 5512</div>
  </div>
  <a class="btn" href="#quote">Get a quote</a>
</header>

<section class="hero" role="img" aria-label="Photo of a modern two-storey home with solar panels on the roof at dusk">
  <h1>Solar Panels for<br>Your Home</h1>
  <a class="btn" href="#quote">Get a quote</a>
</section>

<nav class="nav">
  <a class="active" href="#"><svg width="14" height="14" viewBox="0 0 24 24" fill="#3cc61e"><path d="M12 3l9 8h-3v9h-5v-6h-2v6H6v-9H3z"/></svg>Home</a>
  <a href="#">Products</a>
  <a href="#">Plans &amp; Pricing</a>
  <a href="#">Blog</a>
  <a href="#">Company</a>
  <a href="#">Contact Us</a>
</nav>

<article class="feature" style="left:140px">
  <svg width="56" height="48" viewBox="0 0 56 48" fill="none" stroke="#3cc61e" stroke-width="2.5"><rect x="4" y="8" width="44" height="30" rx="3"/><path d="M4 16h44M10 30h12"/><circle cx="44" cy="36" r="8" fill="#fff"/><path d="M40 36l3 3 5-6"/></svg>
  <h3>Payment solutions<br>for every home</h3>
  <p>Lorem ipsum dolor sit amet conse ctetur adipiscing elit sed do eiusmod tempor incididunt labore.</p>
</article>
<article class="feature" style="left:460px">
  <svg width="56" height="48" viewBox="0 0 56 48" fill="none" stroke="#3cc61e" stroke-width="2.5"><path d="M6 24L28 6l22 18"/><path d="M12 20v22h32V20"/><rect x="22" y="28" width="12" height="14"/><path d="M38 10v6"/></svg>
  <h3>Unrivaled home solar<br>&amp; battery experience</h3>
  <p>Lorem ipsum dolor sit amet conse ctetur adipiscing elit sed do eiusmod tempor incididunt labore.</p>
</article>
<article class="feature feature--accent" style="left:780px">
  <h3>Online Estimate</h3>
  <p>Lorem ipsum dolor sit amet conse ctetur adipiscing elit sed do eiusmod tempor labore.</p>
  <a class="btn btn--dark" href="#quote">Get a quote</a>
</article>

<div class="welcome-photo" role="img" aria-label="Photo of rows of solar panels seen from above"></div>
<div class="welcome-frame" role="img" aria-label="Photo of a white family house with rooftop solar panels and a pool"></div>
<div class="welcome-text">
  <div class="eyebrow">Welcome to VoltaryNX</div>
  <h2>Get residential solar, energy storage Solutions with VoltaryNX</h2>
  <p>Lorem ipsum dolor sit amet, consectetur adipiscing elit, sed do eiusmod tempor incididunt ut labore et dolore magna aliqua. Quis ipsum susp endisse ultrices gravida. Risus commodo viverra maecenas accumsan lacus vel facilisis.</p>
  <p>Lorem ipsum dolor sit amet, consectetur adipiscing elit, sed do eiusmod tempor incididunt ut labore et dolore magna aliqua. Quis ipsum susp endisse ultrices gravida. Risus commodo viverra maecenas accumsan lacus vel facilisis.</p>
  <a class="btn" href="#">Read more</a>
</div>

<div class="section-head" style="top:1884px">
  <div class="eyebrow">What we do</div>
  <h2>Explore going solar with VoltaryNX</h2>
</div>
<article class="service" style="left:128px">
  <div class="photo" role="img" aria-label="Photo of a tiled roof covered with solar panels in warm sunlight" style="background:linear-gradient(135deg,#e0a35a,#a85f2a 50%,#3e4a5c)"></div>
  <h3>Residential Solar<br>Solutions</h3>
  <p>Lorem ipsum dolor sit amet consectetur adipiscing elit sed do eiusmod tempor incididunt ut labore.</p>
  <a class="btn" href="#">Read more</a>
</article>
<article class="service" style="left:450px">
  <div class="photo" role="img" aria-label="Photo of a large commercial solar panel field" style="background:linear-gradient(135deg,#a7705a,#4f5d72 55%,#2c3648)"></div>
  <h3>Commercial Solar<br>Solutions</h3>
  <p>Lorem ipsum dolor sit amet consectetur adipiscing elit sed do eiusmod tempor incididunt ut labore.</p>
  <a class="btn" href="#">Read more</a>
</article>
<article class="service" style="left:772px">
  <div class="photo" role="img" aria-label="Photo of a family sitting together outdoors near their home" style="background:linear-gradient(135deg,#a9c7e0,#c8b59a 55%,#6b7550)"></div>
  <h3>Other VoltaryNX<br>solutions</h3>
  <p>Lorem ipsum dolor sit amet consectetur adipiscing elit sed do eiusmod tempor incididunt ut labore.</p>
  <a class="btn" href="#">Read more</a>
</article>

<section class="quote-band" role="img" aria-label="Dimmed photo of a home terrace at evening">
  <h2>Take control of<br>your energy bills.</h2>
  <p>Lorem ipsum dolor sit amet, consectetur adipiscing elit, sed do eiusmod tempor incididunt ut labore. Quis ipsum suspendisse ultrices gravida. Risus commodo viverra maecenas.</p>
  <a class="btn" href="#quote">Get a quote</a>
  <svg class="abs" style="left:350px;top:200px" width="110" height="80" viewBox="0 0 110 80" fill="none" stroke="#fff" stroke-width="2"><path d="M4 70C40 72 70 50 96 14"/><path d="M84 16l12-2 2 12"/></svg>
</section>

<form class="quote-form" id="quote">
  <h3>Get a free<br>personalized quote</h3>
  <div class="row"><div class="field">First Name</div><div class="field">Last Name</div></div>
  <div class="row"><div class="field">Email</div></div>
  <div class="row"><div class="field">Zipcode</div><div class="field">Phone</div></div>
  <div class="row"><div class="field field--tall">Comments</div></div>
  <label class="check"><span></span>I own my home</label>
  <a class="btn" href="#">Submit now</a>
</form>

<div class="section-head" style="top:3480px">
  <div class="eyebrow">Why VoltaryNX solar?</div>
  <h2>Break the limits of traditional energy</h2>
</div>
<div class="finance-photo" role="img" aria-label="Photo of a senior couple reviewing paperwork at a table"></div>
<div class="finance-box">
  <h3>Flexible financing,<br>with $0 down options*</h3>
  <p>Lorem ipsum dolor sit amet, consectetur adipiscing elit, sed do eiusmod tempor incididunt ut labore et dolore magna aliqua. Quis ipsum suspendisse ultrices gravida. Risus commodo viverra maecenas accumsan lacus vel facilisis.</p>
  <a class="btn" href="#">Read more</a>
</div>

<section class="cta">
  <h2>Questions about solar?</h2>
  <p>Have a no obligation conversation with a solar professional and get answers to any questions or concerns you may have. It's that simple.</p>
  <a class="btn btn--dark" href="#">Lets talk solar</a>
</section>

<footer class="footer">
  <div class="brand">VoltaryNX</div>
  <div class="legal">© 2024 All Rights Reserved.<br>Privacy Policy.</div>
  <div class="footer-col" style="left:360px">
    <h4>Links</h4>
    <ul><li>Products</li><li>Plans &amp; Pricing</li><li>Learn</li><li>Company</li><li>Investors</li></ul>
  </div>
  <div class="footer-col" style="left:570px">
    <h4>Contact Us</h4>
    <div class="contact-line"><svg width="16" height="20" viewBox="0 0 24 30" fill="#3cc61e"><path d="M12 0a11 11 0 0 0-11 11c0 8 11 19 11 19s11-11 11-19A11 11 0 0 0 12 0zm0 15a4 4 0 1 1 0-8 4 4 0 0 1 0 8z"/></svg><span>Location Name<br>Dummy address line<br>Oregon 4433 PS 23334</span></div>
    <div class="contact-line"><svg width="16" height="16" viewBox="0 0 24 24" fill="#3cc61e"><path d="M22 16.9v3a2 2 0 0 1-2.2 2 19.8 19.8 0 0 1-8.6-3.1 19.5 19.5 0 0 1-6-6A19.8 19.8 0 0 1 2.1 4.2 2 2 0 0 1 4.1 2h3a2 2 0 0 1 2 1.7c.1 1 .4 1.9.7 2.8a2 2 0 0 1-.5 2.1L8 9.9a16 16 0 0 0 6 6l1.3-1.3a2 2 0 0 1 2.1-.4c.9.3 1.8.6 2.8.7a2 2 0 0 1 1.8 2z"/></svg><span>(555) 014 2290</span></div>
    <div class="contact-line"><svg width="16" height="14" viewBox="0 0 22 18" fill="none" stroke="#3cc61e" stroke-width="2"><rect x="1" y="1" width="20" height="16" rx="2"/><path d="M1 3l10 7 10-7"/></svg><span>hello@voltarynx.example</span></div>
  </div>
  <div class="footer-col" style="left:810px">
    <h4>Newsletter Sign up</h4>
    <p style="width:260px;font-size:13px">Lorem ipsum dolor sit amet consectetur adipiscing elit sed do eiusmod.</p>
    <div class="newsletter-input"></div>
    <a class="btn" href="#">Sign up</a>
  </div>
</footer>

</body>
</html>
```